Tranquil Pathway Business Card

Logo attached. (will be printing onto thick white/off white textured card)

Double sided business card for two Therapists working at Tranquil Pathway.

Require one design, but with different name and mobile numbers on each card.

Target Market(s)

Medical, Health

Industry/Entity Type

Business

Contact Information for Business Card

Need one business card design, but a separate card for each person - Colin Marchetti and Marieke de Boeckx.

FRONT OF CARD

Logo

Name (Colin Marchetti on one card, Marieke de Boeckx on the other)
Professional Clinical Hypnotherapist

Consulting Rooms (Near Lindqvist Hospital)
482 Brackenfield Road
Dunmore VIC 3987

Colin@TranquilPathway.example.au OR Marieke@TranquilPathway.example.au

Mobile: 0455 872 604 (for Colin) OR
Mobile: 0467 290 518 (for Marieke)

BACK OF CARD

Logo

Website: www.TranquilPathway.example.au

Phone: 1300 958 471

Requirements
Must have
• Text and logo only. No additiional graphics.

```html
<!DOCTYPE html>
<html lang="en">
<head>
<meta charset="utf-8">
<title>Tranquil Pathway – Business Card Back</title>
<link rel="stylesheet" href="https://fonts.googleapis.com/css2?family=Source+Sans+3:wght@400;700&display=swap">
<style>
  :root {
    --paper: #eeefef;
    --navy: #222b5f;
    --icon-disc: #bfbfc1;
    --contact-text: #c9cbd6;
  }
  * { margin: 0; padding: 0; box-sizing: border-box; }
  html, body {
    width: 1200px;
    height: 755px;
    overflow: hidden;
    background: var(--paper);
  }
  .card {
    position: relative;
    width: 1200px;
    height: 755px;
    background: var(--paper);
    font-family: "Source Sans 3", "Myriad Pro", Arial, sans-serif;
  }
  .brand {
    position: absolute;
    left: 307px;
    top: 168px;
    display: flex;
    align-items: center;
    gap: 36px;
  }
  .brand-disc {
    width: 180px;
    height: 180px;
    border-radius: 50%;
    background: var(--navy);
    flex: none;
  }
  .brand-name {
    color: var(--navy);
    font-weight: 700;
    font-size: 56px;
    line-height: 1;
    letter-spacing: 0.5px;
  }
  .contact-band {
    position: absolute;
    left: 0;
    top: 456px;
    width: 1200px;
    height: 299px;
    background: var(--navy);
  }
  .contact-list {
    position: absolute;
    left: 327px;
    top: 33px;
    list-style: none;
  }
  .contact-item {
    display: flex;
    align-items: center;
    height: 54px;
    margin-bottom: 14px;
    color: var(--contact-text);
    font-size: 23px;
  }
  .contact-icon {
    width: 54px;
    height: 54px;
    border-radius: 50%;
    background: var(--icon-disc);
    display: flex;
    align-items: center;
    justify-content: center;
    flex: none;
  }
  .contact-label {
    width: 114px;
    margin-left: 19px;
  }
</style>
</head>
<body>
  <main class="card">
    <div class="brand">
      <div class="brand-disc"></div>
      <div class="brand-name">Tranquil Pathway</div>
    </div>

    <section class="contact-band">
      <ul class="contact-list">
        <li class="contact-item">
          <span class="contact-icon">
            <svg width="20" height="30" viewBox="0 0 20 30" aria-hidden="true">
              <rect x="2" y="1.5" width="16" height="27" rx="3" fill="none" stroke="#ffffff" stroke-width="2"/>
              <line x1="4" y1="6" x2="16" y2="6" stroke="#ffffff" stroke-width="1.5"/>
              <line x1="4" y1="23" x2="16" y2="23" stroke="#ffffff" stroke-width="1.5"/>
            </svg>
          </span>
          <span class="contact-label">Phone:</span>
          <span class="contact-value">1300 958 471</span>
        </li>
        <li class="contact-item">
          <span class="contact-icon">
            <svg width="24" height="24" viewBox="0 0 24 24" aria-hidden="true" fill="none" stroke="#ffffff" stroke-width="1.5">
              <circle cx="12" cy="12" r="10"/>
              <ellipse cx="12" cy="12" rx="4.5" ry="10"/>
              <line x1="2" y1="12" x2="22" y2="12"/>
              <line x1="4" y1="7" x2="20" y2="7"/>
              <line x1="4" y1="17" x2="20" y2="17"/>
            </svg>
          </span>
          <span class="contact-label">Website:</span>
          <span class="contact-value">www.TranquilPathway.example.au</span>
        </li>
      </ul>
    </section>
  </main>
</body>
</html>
```